REAL ESTATE MAILBOX DROP FLYER

I am looking for two flyer designs. One for DL and one for A4 size. My company is a boutique real estate agency that offers a full/high quality service at a very low commission rate.

Key Phrases to be included

A4 Design should have a space for some text and a table in the center (outline below)

Target Market(s)

Home Owners

Industry/Entity Type

Real Estate Agent

Colors
0455a3

Requirements
Must have
• Eye Catching
• Bold
• high end feel
• Color pallette should match the logo
• The feel of the brochures must convey a trustworthy, high end service.
• Must be eye catching and easy to read
• Editable file formats must be supplied

```html
<!DOCTYPE html>
<html lang="en">
<head>
<meta charset="utf-8">
<title>Lowmark Realty – DL Flyer</title>
<link rel="stylesheet" href="https://fonts.googleapis.com/css2?family=Libre+Baskerville:wght@400;700&family=Roboto+Condensed:wght@700&family=Roboto:ital,wght@0,700;1,700;1,900&family=Montserrat:wght@400;500;700&display=swap">
<style>
  :root {
    --navy: #0b3358;
    --navy-deep: #082a4a;
    --gold: #c9a01c;
    --gold-band: #d2a90a;
    --yellow: #f2c52b;
    --white: #ffffff;
    --page: #eef0f2;
    --serif: "Libre Baskerville", Georgia, serif;
    --condensed: "Roboto Condensed", Arial, sans-serif;
    --sans: "Montserrat", Arial, sans-serif;
    --italic: "Roboto", Arial, sans-serif;
  }
  * { box-sizing: border-box; margin: 0; padding: 0; }
  html, body { width: 1200px; height: 1200px; overflow: hidden; background: var(--page); }
  .flyer {
    position: absolute; left: 312px; top: 20px;
    width: 575px; height: 1160px;
    background: var(--white);
    box-shadow: 0 4px 18px rgba(0,0,0,.12);
  }
  .abs { position: absolute; }

  /* header */
  .brand {
    left: 38px; top: 66px; width: 230px;
    font-family: var(--serif); font-weight: 400; color: var(--navy);
    text-align: center; line-height: 1;
  }
  .brand .line1 { font-size: 28px; letter-spacing: .5px; }
  .brand .line2 { font-size: 38px; margin-top: 4px; letter-spacing: .5px; }
  .contact { left: 284px; top: 56px; width: 266px; text-align: left; white-space: nowrap; }
  .contact .lead { font-family: var(--condensed); font-weight: 700; font-size: 20px; line-height: 24px; color: var(--navy); letter-spacing: .1px; }
  .contact .phone { font-family: var(--italic); font-weight: 700; font-size: 35px; line-height: 38px; color: var(--gold); letter-spacing: 1px; }
  .contact .offer { font-family: var(--italic); font-style: italic; font-weight: 700; font-size: 18px; line-height: 24px; color: var(--navy); letter-spacing: .4px; }

  /* photos */
  .photo { display: block; }
  .photo-living { left: 20px; top: 154px; width: 538px; height: 318px;
    background: linear-gradient(180deg, #dcdedf 0%, #c9c8c4 45%, #a48a72 70%, #b9b7b3 100%); }
  .photo-kitchen { left: 20px; top: 481px; width: 272px; height: 179px;
    background: linear-gradient(180deg, #eceeef 0%, #d8d6d2 50%, #a88a68 100%); }
  .photo-bedroom { left: 20px; top: 670px; width: 272px; height: 176px;
    background: linear-gradient(180deg, #eef0f1 0%, #d9dbdd 55%, #6c6e72 100%); }
  .strip { left: 20px; top: 660px; width: 272px; height: 10px; background: var(--navy); }

  /* offer panel */
  .offer-panel { left: 292px; top: 481px; width: 266px; height: 365px; background: var(--navy); }
  .rate { left: 16px; top: 112px; font-family: var(--sans); font-weight: 700; color: var(--yellow); line-height: 1; }
  .rate .num { font-size: 74px; }
  .rate .pct { position: absolute; left: 36px; top: 6px; font-size: 30px; }
  .service { left: 113px; top: 82px; font-family: var(--sans); font-weight: 500; color: var(--white); font-size: 21px; line-height: 1.12; letter-spacing: .8px; }
  .commission { left: 58px; top: 164px; font-family: var(--sans); font-weight: 500; color: var(--yellow); font-size: 21.5px; letter-spacing: 1.2px; white-space: nowrap; }
  .rule { left: 14px; width: 238px; height: 1px; background: rgba(255,255,255,.85); }
  .save { left: 14px; top: 222px; width: 238px; font-family: var(--serif); font-weight: 400; color: var(--white); font-size: 64px; line-height: 1; letter-spacing: 6px; }
  .save-sub { left: 14px; top: 290px; font-family: var(--serif); font-weight: 400; color: var(--white); font-size: 29px; line-height: 1.05; white-space: nowrap; }

  /* band */
  .band { left: 20px; top: 858px; width: 538px; height: 64px; background: var(--gold-band);
    display: flex; align-items: center; justify-content: center; gap: 12px; }
  .band p { font-family: var(--italic); font-style: italic; font-weight: 700; color: var(--white); font-size: 24px; letter-spacing: .4px; }

  /* footer */
  .footer { left: 20px; top: 922px; width: 538px; height: 226px; background: var(--navy-deep); color: var(--white); text-align: center; }
  .touch { margin-top: 30px; display: flex; align-items: center; justify-content: center; gap: 10px; font-family: var(--sans); font-size: 20px; font-weight: 500; }
  .icons { margin-top: 14px; display: flex; justify-content: center; gap: 16px; }
  .icons span { width: 52px; height: 52px; border: 2px solid var(--white); border-radius: 50%; display: flex; align-items: center; justify-content: center; }
  .details { margin-top: 14px; font-family: var(--sans); font-size: 18px; line-height: 1.48; letter-spacing: .6px; }
  .details b { font-weight: 700; }
</style>
</head>
<body>
<main class="flyer">
  <header>
    <div class="abs brand"><div class="line1">LOWMARK</div><div class="line2">REALTY</div></div>
    <div class="abs contact">
      <p class="lead">CONTACT MARCUS TODAY ON</p>
      <p class="phone">0400-718-264</p>
      <p class="offer">for a FREE APPRAISAL!</p>
    </div>
  </header>

  <div class="abs photo photo-living" role="img" aria-label="Bright living room with grey sofas and a dining area"></div>
  <div class="abs photo photo-kitchen" role="img" aria-label="Open plan kitchen and lounge"></div>
  <div class="abs strip"></div>
  <div class="abs photo photo-bedroom" role="img" aria-label="Styled master bedroom"></div>

  <section class="abs offer-panel">
    <div class="abs rate"><span class="num">1</span><span class="pct">%</span></div>
    <p class="abs service">FULL<br>SERVICE<br>AGENCY,</p>
    <p class="abs commission">COMMISSION</p>
    <div class="abs rule" style="top:213px"></div>
    <p class="abs save">SAVE</p>
    <p class="abs save-sub">Thousands On<br>Commissions!</p>
    <div class="abs rule" style="top:362px"></div>
  </section>

  <div class="abs band">
    <svg width="46" height="38" viewBox="0 0 46 38" fill="none" stroke="#fff" stroke-width="2">
      <rect x="4" y="20" width="30" height="14" transform="rotate(-12 19 27)"/>
      <rect x="8" y="13" width="30" height="14" transform="rotate(-12 23 20)"/>
      <rect x="12" y="6" width="30" height="14" transform="rotate(-12 27 13)"/>
      <circle cx="27" cy="13" r="3.5"/>
    </svg>
    <p>More Money in YOUR Pocket!</p>
  </div>

  <footer class="abs footer">
    <div class="touch">
      <svg width="62" height="10" viewBox="0 0 62 10"><line x1="0" y1="5" x2="56" y2="5" stroke="#fff" stroke-width="1.5"/><path d="M52 1 L61 5 L52 9 Z" fill="#fff"/></svg>
      <span>Get in Touch</span>
      <svg width="62" height="10" viewBox="0 0 62 10"><line x1="6" y1="5" x2="62" y2="5" stroke="#fff" stroke-width="1.5"/><path d="M10 1 L1 5 L10 9 Z" fill="#fff"/></svg>
    </div>
    <div class="icons">
      <span><svg width="26" height="26" viewBox="0 0 24 24" fill="#fff"><path d="M6.6 10.8a15.1 15.1 0 0 0 6.6 6.6l2.2-2.2c.3-.3.7-.4 1-.2 1.1.4 2.3.6 3.6.6.6 0 1 .4 1 1V20c0 .6-.4 1-1 1A17 17 0 0 1 3 4c0-.6.4-1 1-1h3.5c.6 0 1 .4 1 1 0 1.3.2 2.5.6 3.6.1.3 0 .7-.2 1z"/></svg></span>
      <span><svg width="26" height="22" viewBox="0 0 26 22" fill="none" stroke="#fff" stroke-width="2"><rect x="2" y="3" width="22" height="16"/><path d="M2 3 L13 12 L24 3"/></svg></span>
      <span><svg width="28" height="28" viewBox="0 0 28 28" fill="none" stroke="#fff" stroke-width="1.6"><circle cx="14" cy="14" r="11"/><ellipse cx="14" cy="14" rx="5" ry="11"/><line x1="3" y1="14" x2="25" y2="14"/><path d="M5 8h18M5 20h18"/></svg></span>
    </div>
    <div class="details">
      <p>Marcus Ellery - <b>0400-718-264</b></p>
      <p>marcus@lowmarkrealty.com.au</p>
      <p>www.lowmarkrealty.com.au</p>
    </div>
  </footer>
</main>
</body>
</html>
```